Simple, Professional and neat business card design for Vendralo Inc.

We're looking to re-vamp our business card design. We're a supplier of innovative feed ingredients for the North American animal agriculture industry. We are located in Lucknow, Ontario, Canada and our flagship product is a product that prevents milk fever in dairy cows when the calve, it is fed before calving and is very effective compared to other alternatives available on the market today.

Our company has Danish roots and we import all of our product from our Danish partner/manufacturer in Denmark. We like our design to embrace high professionalism while remaining neat and simple.

Target Market(s)

B2B, Feed Mills, Veterinary Clinics, Large integrators/producers,

Industry/Entity Type

Agribusiness

Contact Information for Business Card

We like the rounded corners because they make the card easy to sit in a wallet and not many use it so it makes the card stand out, just possibly something to take account for during the design.

As you can also see on the sliders below, looking for a that simple but proffesional scandinavian design.

Requirements
Nice to have
• Rounded corners
Should not have
• Too vibrant

```html
<!DOCTYPE html>
<html lang="en">
<head>
<meta charset="utf-8">
<title>Vendralo Inc. Business Card</title>
<link rel="stylesheet" href="https://fonts.googleapis.com/css2?family=Lato:wght@900&family=Barlow+Condensed:wght@300;400;500&display=swap">
<style>
  :root {
    --brand-blue: #0355a6;
    --brand-blue-dark: #0a3f80;
    --gold: #d9c08a;
    --gold-light: #efe2bf;
    --ink: #1c1c1c;
    --white: #ffffff;
    --canvas: #ffffff;
  }
  * { margin: 0; padding: 0; box-sizing: border-box; }
  html, body { width: 1200px; height: 1200px; overflow: hidden; background: var(--canvas); }
  .canvas { position: relative; width: 1200px; height: 1200px; }

  .card { position: absolute; left: 190px; width: 840px; height: 480px; border-radius: 40px; overflow: hidden; }
  .card--front { top: 82px; background: var(--brand-blue); }
  .card--back { top: 652px; background: var(--white); border: 3px solid var(--brand-blue); }

  .wordmark { position: absolute; font-family: "Lato", sans-serif; font-weight: 900; color: var(--white); letter-spacing: -1px; line-height: 1; white-space: nowrap; }
  .tagline { position: absolute; font-family: "Barlow Condensed", sans-serif; font-weight: 300; color: var(--white); line-height: 1; white-space: nowrap; }

  .logo-mark { position: absolute; border-radius: 50%; background: radial-gradient(circle at 50% 35%, var(--gold-light), var(--gold)); border: 4px solid var(--white); }

  /* front */
  .card--front .logo-mark { left: 345px; top: 58px; width: 150px; height: 150px; }
  .card--front .wordmark { left: 0; width: 840px; text-align: center; top: 243px; font-size: 61px; }
  .card--front .tagline { left: 0; width: 840px; text-align: center; top: 300px; font-size: 30px; }

  .features { position: absolute; top: 385px; left: 48px; display: flex; gap: 34px; align-items: center; }
  .feature { display: flex; align-items: center; gap: 8px; font-family: "Barlow Condensed", sans-serif; font-weight: 500; font-size: 27px; color: var(--white); white-space: nowrap; }
  .feature svg { width: 44px; height: 44px; flex: none; }

  /* back */
  .back-band { position: absolute; left: -3px; top: -3px; width: 843px; height: 312px; background: var(--brand-blue); }
  .card--back .logo-mark { left: 90px; top: 48px; width: 122px; height: 122px; }
  .card--back .wordmark { left: 241px; top: 76px; font-size: 69px; }
  .card--back .tagline { left: 244px; top: 155px; font-size: 27px; line-height: 32px; }
  .person-name { position: absolute; right: 87px; top: 253px; font-family: "Barlow Condensed", sans-serif; font-weight: 500; font-size: 39px; color: var(--white); line-height: 1; }

  .contact { position: absolute; top: 320px; font-family: "Barlow Condensed", sans-serif; font-weight: 400; font-size: 24px; line-height: 28px; color: var(--ink); }
  .contact--left { left: 87px; }
  .contact--right { right: 87px; text-align: right; }
</style>
</head>
<body>
<div class="canvas">

  <section class="card card--front">
    <div class="logo-mark" aria-hidden="true"></div>
    <h1 class="wordmark">VENDRALO INC.</h1>
    <p class="tagline">Protecting the health of your animals</p>
    <ul class="features">
      <li class="feature">
        <svg viewBox="0 0 44 44" aria-hidden="true">
          <path d="M22 4 L38 9 V22 C38 31 31 37 22 41 C13 37 6 31 6 22 V9 Z" fill="#1d87d4" stroke="#0a3f80" stroke-width="2"/>
          <circle cx="22" cy="23" r="6" fill="#d9c08a"/>
        </svg>
        Preventative care
      </li>
      <li class="feature">
        <svg viewBox="0 0 44 44" aria-hidden="true">
          <circle cx="22" cy="22" r="15" fill="none" stroke="#1d87d4" stroke-width="3"/>
          <line x1="6" y1="38" x2="38" y2="6" stroke="#d9c08a" stroke-width="3" stroke-linecap="round"/>
          <path d="M38 6 L30 8 L36 14 Z" fill="#d9c08a"/>
        </svg>
        High-perfomance
      </li>
      <li class="feature">
        <svg viewBox="0 0 44 44" aria-hidden="true">
          <circle cx="22" cy="22" r="18" fill="#0a4d98" stroke="#0a3f80" stroke-width="3"/>
          <line x1="9" y1="9" x2="35" y2="35" stroke="#1d87d4" stroke-width="3"/>
        </svg>
        Prescription free
      </li>
    </ul>
  </section>

  <section class="card card--back">
    <div class="back-band"></div>
    <div class="logo-mark" aria-hidden="true"></div>
    <h2 class="wordmark">VENDRALO INC.</h2>
    <p class="tagline">Distributor of innovate feed ingredients<br>and other preventative products</p>
    <p class="person-name">Mikkel Sørvang</p>
    <address class="contact contact--left" style="font-style:normal">
      mikkel@vendralo.com<br>
      www.vendralo.com<br>
      Box 412, Harlow Creek,<br>
      Ontario Canada N0X 1A0
    </address>
    <p class="contact contact--right">
      Mobil: 519-555-0147<br>
      Office: 519-555-0182<br>
      Toll free: 888-555-0129<br>
      Fax: 519-555-0163
    </p>
  </section>

</div>
</body>
</html>
```